Business card for a plastic surgeon

i need a business card for a plastic surgeon. I have two adresses. The card should communicate safety, simmetry, beauty and with soft colors.
What i want in the card:
- my logo: Letters "R"and "B" (picture uploaded)
- my name: Renato Bastiani
- my registration: CRM 507 219
- my adresses and phone numbers (2):
- Av Dr Teixeira Lopes, 2710, sala 305 - Vila Olímpia | São Paulo/ SP - Phone: 11 4172-5036
- Al. Itapeva, 47, 3 andar - Alphaville | Barueri/ SP - Phone: 11 6350-2481

- my social network: site, facebook and instagram

Target Market(s)

people (95% girls and women) that want cosmetic procedures and plastic surgery

Industry/Entity Type

Business

Contact Information for Business Card

The card should communicate safety, simmetry, beauty and with soft colors.
Beige, brown, gray, rosy are some options. Color is free

Font styles to use
Serif

Requirements
Must have
• - my logo: Letters "R"and "B" (picture uploaded)
• - my name: Renato Bastiani
• - my registration: CRM 507 219
• - my adresses and phone numbers (2):
• - Av Dr Teixeira Lopes, 2710, sala 305 - Vila Olímpia | São Paulo/ SP - Phone: 11 4172-5036
• - Al. Itapeva, 47, 3 andar - Alphaville | Barueri/ SP - Phone: 11 6350-2481
• - my social network: site, facebook and instagram
Should not have
• other images (only my logo)

```html
<!DOCTYPE html>
<html lang="pt-BR">
<head>
<meta charset="utf-8">
<title>Dr. Renato Bastiani – Cartão de Visita</title>
<link href="https://fonts.googleapis.com/css2?family=Cormorant+Garamond:wght@500;600&family=Source+Sans+3:ital,wght@0,400;0,600;1,400&display=swap" rel="stylesheet">
<style>
  :root {
    --backdrop: #262626;
    --paper: #ffffff;
    --taupe: #a38a72;
    --slate: #686868;
    --ink: #4f4f4f;
    --rule: #c9c9c9;
  }
  * { box-sizing: border-box; margin: 0; padding: 0; }
  html, body { width: 1200px; height: 987px; overflow: hidden; }
  body { background: var(--backdrop); position: relative; font-family: "Source Sans 3", Arial, sans-serif; }

  .card { position: absolute; left: 292px; width: 616px; height: 352px; overflow: hidden; box-shadow: 0 4px 14px rgba(0,0,0,.5); }
  .card--front { top: 130px; background: var(--paper); }
  .card--back { top: 505px; background: var(--taupe); }
  .card svg.shape { position: absolute; inset: 0; width: 616px; height: 352px; }

  /* Front */
  .brand-mark { position: absolute; left: 0; width: 284px; top: 112px; text-align: center; white-space: nowrap;
    font-family: "Cormorant Garamond", Georgia, serif; font-weight: 500; font-size: 40px; color: var(--taupe); }
  .brand-name { position: absolute; left: 0; width: 284px; top: 196px; text-align: center; white-space: nowrap;
    font-family: "Cormorant Garamond", Georgia, serif; font-weight: 500; font-size: 24px; line-height: 28px; color: var(--taupe); }
  .brand-role { position: absolute; left: 0; width: 284px; top: 226px; text-align: center; white-space: nowrap;
    font-family: "Cormorant Garamond", Georgia, serif; font-weight: 600; font-size: 12px; line-height: 16px; color: var(--taupe); letter-spacing: 3px; }
  .divider { position: absolute; left: 308px; top: 69px; width: 1px; height: 206px; background: var(--rule); }
  .contact { position: absolute; left: 335px; top: 64px; color: var(--ink); font-size: 16.4px; line-height: 22px; white-space: nowrap; }
  .contact h2 { font-size: 22px; font-weight: 600; color: var(--taupe); margin-bottom: 9px; }
  .contact .address + .address { margin-top: 8px; }
  .contact .label { color: var(--taupe); font-weight: 600; }
  .registration { position: absolute; left: 346px; top: 328px; color: #fff; font-style: italic; font-size: 16px; line-height: 20px; white-space: nowrap; }

  /* Back */
  .back-name { position: absolute; left: 20px; width: 340px; top: 146px; text-align: center; color: #fff; white-space: nowrap;
    font-family: "Cormorant Garamond", Georgia, serif; font-weight: 500; font-size: 30px; letter-spacing: .5px; }
  .back-role { position: absolute; left: 20px; width: 340px; top: 182px; text-align: center; color: #fff; white-space: nowrap;
    font-family: "Cormorant Garamond", Georgia, serif; font-weight: 600; font-size: 14px; letter-spacing: 3.6px; }
  .social { position: absolute; left: 52px; width: 273px; top: 210px; height: 20px; display: flex; align-items: center; gap: 4px; }
  .social .line { flex: 1; height: 1px; background: rgba(255,255,255,.8); }
  .social .dot { width: 19px; height: 19px; border-radius: 50%; background: #fff; }
  .back-mark { position: absolute; left: 420px; width: 180px; top: 180px; text-align: center; color: #fff; white-space: nowrap;
    font-family: "Cormorant Garamond", Georgia, serif; font-weight: 500; font-size: 34px; }
</style>
</head>
<body>

<section class="card card--front">
  <svg class="shape" viewBox="0 0 616 352" aria-hidden="true">
    <path d="M0,300 C100,304 180,336 280,322 C360,310 450,292 616,290 L616,304 C450,306 360,316 280,330 C180,346 100,330 0,322 Z" fill="var(--slate)"/>
    <path d="M0,330 C100,336 180,352 280,338 C360,326 450,312 616,310 L616,352 L0,352 Z" fill="var(--taupe)"/>
  </svg>

  <div class="brand-mark">Bastiani</div>
  <div class="brand-name">DR. RENATO BASTIANI</div>
  <div class="brand-role">CIRURGIÃO PLÁSTICO</div>

  <div class="divider"></div>

  <div class="contact">
    <h2>Renato Bastiani</h2>
    <p class="address">Av Dr Teixeira Lopes, 2710<br>sala 305 - Vila Olímpia<br>São Paulo/ SP<br><span class="label">Phone:</span> 11 4172-5036</p>
    <p class="address">Al. Itapeva, 47<br>3 andar - Alphaville | Barueri/ SP<br><span class="label">Phone:</span> 11 6350-2481</p>
  </div>

  <p class="registration">Registration: CRM 507 219</p>
</section>

<section class="card card--back">
  <svg class="shape" viewBox="0 0 616 352" aria-hidden="true">
    <path d="M505,0 C430,90 430,250 356,352 L616,352 L616,0 Z" fill="var(--slate)"/>
    <path d="M488,0 L505,0 C430,90 420,250 356,352 L336,352 C410,250 420,90 488,0 Z" fill="#fff"/>
  </svg>

  <div class="back-name">DR. RENATO BASTIANI</div>
  <div class="back-role">CIRURGIÃO PLÁSTICO</div>
  <div class="social">
    <span class="line"></span><span class="dot"></span><span class="dot"></span><span class="line"></span>
  </div>

  <div class="back-mark">Bastiani</div>
</section>

</body>
</html>
```